Business Card Design

Our team name is MERIDIAN ALLIANCE and that should be the prominent part of the business card, we would also like to have an infinity sign incorporated with the name.

We are Realtors with HO/LEX and must have the HO/LEX logo on the front of the card along with our Team name / logo. HO/LEX logo can be a watermark or a smaller portion of the whole design. Please choose any of the HO/LEX logos included here.

We would like to have a two sided card and on the back something like "the highest compliment that you can give me is the referral of your friend and family member" or similar statement.
We have other industry logos that also have to be on the back of the card (included below). These logos should be VERY small as they are a requirement but not the focus of the card in any way.

Contact Information for Business Card

Marla Pettigrew
555-738-2046 Cell
555-619-4873 Fax
marla@marlapettigrew.example

HO/LEX Realty Center
40735 Bramwick
Cypress, Tx 70815

each office independently owned and operated

Font styles to use
Sans Serif
Script

Requirements
Must have
• The attached industry logos are must have features. The HO/LEX logo must be on the front of the card. The other two can be front or back. All can be color or black and white.

Must state - "Each office independently owned and operated" somewhere front or back of card. small print is fine.
Nice to have
• An infinity sign incorporated into the design.

```html
<!DOCTYPE html>
<html lang="en">
<head>
<meta charset="utf-8">
<title>Meridian Alliance – Business Card Back</title>
<link rel="stylesheet" href="https://fonts.googleapis.com/css2?family=Mulish:wght@800&display=swap">
<style>
  :root {
    --paper: #ffffff;
    --navy-text: #1f3a6b;
    --band-blue: #1b4f9c;
    --band-blue-light: #5d9ad8;
    --band-red: #e0312f;
    --band-red-light: #f0644a;
    --sky-light: #cfe6f7;
    --badge-dark: #1a1a1a;
    --badge-grey: #9a9a9a;
    --badge-fill: #f2f2f2;
  }
  html, body {
    margin: 0;
    padding: 0;
    overflow: hidden;
    background: var(--paper);
  }
  .card {
    position: relative;
    width: 1200px;
    height: 686px;
    background: var(--paper);
    overflow: hidden;
  }
  .referral-quote {
    position: absolute;
    top: 112px;
    left: 0;
    width: 1200px;
    margin: 0;
    text-align: center;
    font-family: "Mulish", sans-serif;
    font-weight: 800;
    font-size: 44px;
    line-height: 50px;
    color: var(--navy-text);
    letter-spacing: 0.2px;
    z-index: 2;
  }
  .swoosh {
    position: absolute;
    top: 0;
    left: 0;
    width: 1200px;
    height: 686px;
    z-index: 1;
  }
  .industry-badges {
    position: absolute;
    top: 563px;
    left: 431px;
    display: flex;
    gap: 42px;
    align-items: flex-start;
    z-index: 2;
  }
  .badge-housing {
    width: 92px;
    height: 96px;
    background: var(--badge-dark);
  }
  .badge-listing {
    width: 194px;
    height: 92px;
    box-sizing: border-box;
    border: 2px solid var(--badge-grey);
    background: var(--badge-fill);
  }
</style>
</head>
<body>
  <main class="card">
    <svg class="swoosh" viewBox="0 0 1200 686" aria-hidden="false">
      <defs>
        <linearGradient id="blueBand" x1="0" x2="1" y1="0" y2="0">
          <stop offset="0" stop-color="var(--band-blue)"/>
          <stop offset="0.55" stop-color="var(--band-blue-light)"/>
          <stop offset="0.8" stop-color="var(--band-blue)"/>
          <stop offset="1" stop-color="var(--band-blue)"/>
        </linearGradient>
        <linearGradient id="scene" x1="0" x2="1" y1="0" y2="0">
          <stop offset="0" stop-color="#4a8fd0"/>
          <stop offset="0.35" stop-color="#a9cdee"/>
          <stop offset="0.65" stop-color="var(--sky-light)"/>
          <stop offset="1" stop-color="#ffffff" stop-opacity="0"/>
        </linearGradient>
        <linearGradient id="redBand" x1="0" x2="1" y1="0" y2="0">
          <stop offset="0" stop-color="var(--band-red-light)"/>
          <stop offset="0.5" stop-color="var(--band-red)"/>
          <stop offset="1" stop-color="var(--band-red)"/>
        </linearGradient>
      </defs>
      <path class="band-blue" fill="url(#blueBand)"
        d="M0,211 C200,255 400,335 560,335 C700,332 800,268 920,266 C1040,265 1120,276 1200,282
           L1200,300 C1000,300 820,340 620,372 C450,392 250,370 0,300 Z"/>
      <path class="band-scene" role="img" aria-label="Photo of a glass-roofed building reflected in the curve"
        fill="url(#scene)"
        d="M0,262 C200,300 400,350 560,350 C700,348 820,300 1000,290 C1100,286 1160,290 1200,292
           L1200,300 C1000,302 820,344 620,376 C450,396 250,378 0,318 Z"/>
      <path class="band-red" fill="url(#redBand)"
        d="M0,312 C250,378 450,398 620,378 C820,352 1000,312 1200,298
           L1200,306 C1000,322 820,372 620,400 C440,420 240,406 0,346 Z"/>
    </svg>

    <p class="referral-quote">"the highest compliment that you can give me is the<br>referral of your friend and family member"</p>

    <div class="industry-badges">
      <div class="badge-housing" role="img" aria-label="Equal housing badge"></div>
      <div class="badge-listing" role="img" aria-label="Industry listing service badge"></div>
    </div>
  </main>
</body>
</html>
```